Company/Customer - Leave-Behind Card

Need a Standard size post card 4x6
Hard Stock Paper, Glossy
This will be a logo embossed card that is left behind with our customers
after work is completed, and also for potential customers with additional needs
You completed our Company design, for us,
We are TMZ Pane Crafters LLC
I will upload logos and some info we need to have on th eproject
Target Market(s)
We are a professional company (Husband, Wife Team) specializing in Installation of premium Window fashions. Drapery, Shades, Blinds and custom window treatments.
We also specialize in project planning, Consultation, take down, put up services and will also provide some designing but are not specialists in the field. We can also take care of installing/hanging other items, such as Mirrors, paintings, etc...
We want to target both current customers, and potential customers for which leads will be generated
Industry/Entity Type
Professional Service
Font styles to use
Colors
Designer to choose colors to be used in the design.
Requirements
Must have
- Our company logo, our partner logos but not as prominent, our skill sets and certifications. Mission statement
Nice to have
- Eye catching colors, simple design, not to busy, or have to much to look at.
- I would like to see the logos embossed or maybe a looking glass effect.
Should not have
- Too busy, or too much to look at

```html
<!DOCTYPE html>
<html lang="en">
<head>
<meta charset="utf-8">
<title>TMZ Pane Crafters LLC – Leave-Behind Card</title>
<link rel="stylesheet" href="https://fonts.googleapis.com/css2?family=Open+Sans:wght@400;600;700&display=swap">
<style>
  :root {
    --navy: #1f3f8a;
    --navy-deep: #1a2f6e;
    --blue: #2c58a6;
    --sky: #3f8fd0;
    --paper: #f4f5f7;
    --grey: #c9ccd1;
    --ink: #1b1b1b;
    --white: #ffffff;
    --backdrop: #2b2c2e;
    --badge: #dfe2e7;
  }
  * { margin: 0; padding: 0; box-sizing: border-box; }
  html, body { width: 880px; height: 1200px; overflow: hidden; }
  body { background: var(--backdrop); font-family: "Open Sans", Arial, sans-serif; position: relative; }

  .card { position: absolute; left: 54px; width: 774px; height: 515px; background: var(--paper); overflow: hidden; box-shadow: 0 6px 18px rgba(0,0,0,.45); }
  .card--front { top: 58px; }
  .card--back { top: 628px; }
  .abs { position: absolute; }

  /* front */
  .brand { left: 52px; top: 44px; display: flex; align-items: center; gap: 12px; }
  .brand__mark { width: 40px; height: 40px; background: var(--sky); flex: none; }
  .brand__name { font-size: 23px; font-weight: 600; color: var(--navy); line-height: 1.1; }
  .band-blue { left: 0; top: 118px; width: 774px; height: 304px; background: linear-gradient(90deg, var(--navy) 0%, var(--blue) 55%, var(--sky) 100%); }
  .band-grey { left: 0; top: 422px; width: 774px; height: 93px; background: linear-gradient(180deg, #e4e6e9, var(--grey)); }
  .tagline { left: 38px; top: 134px; color: var(--white); font-size: 14.5px; font-weight: 700; line-height: 20px; }
  .rule { height: 2px; background: var(--white); }
  .rule--tag { left: 38px; top: 179px; width: 124px; }
  .services { left: 38px; top: 197px; color: var(--white); font-size: 19.5px; font-weight: 700; line-height: 26px; list-style: none; }
  .services li { position: relative; padding-left: 25px; }
  .services li + li { margin-top: 3px; }
  .services svg { position: absolute; left: 0; top: 5px; }
  .extra { left: 39px; top: 339px; color: var(--white); }
  .extra__title { font-size: 17px; font-weight: 700; border-bottom: 2px solid var(--white); display: inline-block; padding-bottom: 1px; }
  .extra__text { font-size: 13.5px; line-height: 18px; margin-top: 7px; }
  .contacts { left: 38px; top: 436px; display: grid; grid-template-columns: 178px auto; row-gap: 7px; font-size: 19.5px; font-weight: 700; color: var(--ink); }
  .contacts div { display: flex; align-items: center; gap: 10px; height: 26px; }

  .photo { position: absolute; border-radius: 50%; border: 2px solid var(--white); }
  .photo--shades { left: 298px; top: -50px; width: 464px; height: 464px; background: radial-gradient(circle at 55% 40%, #f3efe6, #cdbfa5 60%, #9c8a70); }
  .photo--screen { left: 263px; top: 238px; width: 152px; height: 152px; background: radial-gradient(circle at 40% 40%, #9aa1a0, #5f6a67); }
  .photo--sheer { left: 378px; top: 306px; width: 160px; height: 160px; background: radial-gradient(circle at 50% 40%, #e8ecef, #9aa3a8); }
  .photo--bath { left: 534px; top: 278px; width: 216px; height: 216px; background: radial-gradient(circle at 50% 45%, #f7f8fa, #cfd6dd); }

  /* back */
  .photo--patio { left: 26px; top: -44px; width: 408px; height: 408px; background: radial-gradient(circle at 45% 40%, #c6d4e1, #8796a4 65%, #5d6a76); }
  .photo--arched { left: 24px; top: 294px; width: 188px; height: 188px; background: radial-gradient(circle at 50% 40%, #f6f1e6, #cbbda4); }
  .photo--blinds { left: 246px; top: 272px; width: 152px; height: 152px; background: radial-gradient(circle at 50% 40%, #efe3cc, #b49a78); }
  .photo--living { left: 202px; top: 368px; width: 120px; height: 120px; background: radial-gradient(circle at 50% 40%, #e9edf0, #a9b2b8); }
  .band-mission { left: 380px; top: 194px; width: 394px; height: 96px; background: linear-gradient(90deg, var(--blue), var(--sky)); }
  .headline { left: 457px; top: 30px; color: var(--navy-deep); font-size: 18px; font-weight: 700; line-height: 21px; }
  .rule--head { left: 458px; top: 78px; width: 130px; background: var(--sky); }
  .offer { left: 459px; top: 94px; width: 290px; color: var(--ink); }
  .offer__title { font-size: 16px; font-weight: 700; line-height: 22px; }
  .offer__text { font-size: 12.6px; line-height: 17px; margin-top: 2px; }
  .mission { left: 457px; top: 204px; width: 250px; color: var(--white); }
  .mission__title { font-size: 16px; font-weight: 700; }
  .mission__text { font-size: 10.8px; line-height: 15px; margin-top: 7px; }
  .badge { position: absolute; background: var(--badge); border-radius: 6px; }
</style>
</head>
<body>

<section class="card card--front">
  <div class="abs band-blue"></div>
  <div class="abs band-grey"></div>

  <div class="abs brand">
    <span class="brand__mark"></span>
    <span class="brand__name">TMZ Pane<br>Crafters LLC</span>
  </div>

  <p class="abs tagline">Professional Installation Of<br>Hard And Soft Window treatments</p>
  <div class="abs rule rule--tag"></div>

  <ul class="abs services">
    <li><svg width="18" height="16" viewBox="0 0 18 16"><path d="M1 9l5 5L17 1" fill="none" stroke="#fff" stroke-width="2.4"/></svg>SHUTTERS | SHADES<br>BLINDS | DRAPERY</li>
    <li><svg width="18" height="16" viewBox="0 0 18 16"><path d="M1 9l5 5L17 1" fill="none" stroke="#fff" stroke-width="2.4"/></svg>INDOOR / OUTDOOR<br>RESIDENTIAL &amp;<br>COMMERCIAL</li>
  </ul>

  <div class="abs extra">
    <span class="extra__title">We also Provide</span>
    <p class="extra__text">New Construction Project Planning<br>and Consultation Services</p>
  </div>

  <div class="photo photo--shades" role="img" aria-label="Bright room with tall windows fitted with beige roman shades"></div>
  <div class="photo photo--screen" role="img" aria-label="Close view of a woven screen shade beside a potted plant"></div>
  <div class="photo photo--sheer" role="img" aria-label="Sheer horizontal shades in a modern interior"></div>
  <div class="photo photo--bath" role="img" aria-label="Bathroom with freestanding tub and white vertical sheers"></div>

  <div class="abs contacts">
    <div><svg width="18" height="18" viewBox="0 0 18 18"><rect x="2" y="3" width="14" height="14" fill="none" stroke="#2c58a6" stroke-width="1.6"/><path d="M5 6h2M11 6h2M5 10h2M11 10h2M8 13h2v4H8z" stroke="#2c58a6" stroke-width="1.6"/></svg>555-310-4817</div>
    <div><svg width="20" height="20" viewBox="0 0 20 20"><circle cx="10" cy="10" r="8.5" fill="none" stroke="#1f3f8a" stroke-width="1.6"/><path d="M7 5.5l2 2-1 1.5c.6 1.4 1.6 2.4 3 3l1.5-1 2 2-1.3 1.5c-3.5-.3-6.9-3.7-7.2-7.2z" fill="#1f3f8a"/></svg>555-274-9036</div>
    <div><svg width="18" height="18" viewBox="0 0 18 18"><rect x="5" y="1" width="8" height="5" fill="#2c58a6"/><rect x="1" y="6" width="16" height="7" rx="1.5" fill="#2c58a6"/><rect x="5" y="11" width="8" height="6" fill="#fff" stroke="#2c58a6" stroke-width="1.4"/></svg>555-619-2748</div>
    <div><svg width="20" height="16" viewBox="0 0 20 16"><rect x="1" y="2" width="18" height="12" fill="none" stroke="#1f3f8a" stroke-width="1.6"/><path d="M1 2l9 7 9-7" fill="none" stroke="#1f3f8a" stroke-width="1.6"/></svg>hello@tmzpanecrafters.com</div>
  </div>
</section>

<section class="card card--back">
  <div class="abs band-mission"></div>

  <div class="photo photo--patio" role="img" aria-label="Covered patio with an outdoor solar screen"></div>
  <div class="photo photo--arched" role="img" aria-label="Living room with arched windows and white plantation shutters"></div>
  <div class="photo photo--blinds" role="img" aria-label="Wood blinds lowered over a row of windows"></div>
  <div class="photo photo--living" role="img" aria-label="Sunroom with sheer shades and a sectional sofa"></div>

  <h2 class="abs headline">FAMILY OWNED AND OPERATED<br>TEXAS BUSINESS</h2>
  <div class="abs rule rule--head"></div>

  <div class="abs offer">
    <p class="offer__title">NEW BUILD, RENOVATING,<br>REDECORATING.</p>
    <p class="offer__text">We can also hang your your Mirrors, Paintings<br>and Flat Panel TV's, or any other large items<br>needing to be mounted and/or anchored.</p>
  </div>

  <div class="abs mission">
    <p class="mission__title">Mission statement</p>
    <p class="mission__text">We strive to provide you the most professional<br>installation services available for your home and<br>business.</p>
  </div>

  <div class="badge" style="left:436px;top:312px;width:180px;height:66px"></div>
  <div class="badge" style="left:628px;top:318px;width:116px;height:54px"></div>
  <div class="badge" style="left:402px;top:390px;width:150px;height:40px"></div>
  <div class="badge" style="left:566px;top:390px;width:172px;height:40px"></div>
  <div class="badge" style="left:362px;top:444px;width:58px;height:30px"></div>
  <div class="badge" style="left:428px;top:442px;width:116px;height:34px"></div>
  <div class="badge" style="left:550px;top:444px;width:126px;height:30px"></div>
  <div class="badge" style="left:682px;top:442px;width:60px;height:32px"></div>
</section>

</body>
</html>
```